Box Design for Organic Bamboo Hooded Baby Bath Towels

Box size 25 x 18 x 6cm, attached PDF from supplier for reference, and our logo

We need a box designed for a new company based in Orange County, called Lumo Little Ones. Our company specializes in quality, upscale, health conscious products for infants, babies and toddlers. Our first product launching is a hooded bath towel made of organic bamboo. We would like to see a design that signifies purity, simplicity, safety, and elegance. The colors we like are white, blue (like the shade in our logo attached), greens, and grays.

Front of box:
Needs to include logo

Key Points:
*Unbleached, chemical & toxin free
*Hypoallergenic and Antibacterial
*Three times more absorbent than cotton
*Eco Friendly

Somewhere on the front it needs to note sizing: 30x30 inches
Includes bonus wash cloth

Back of Box:

Do you ever find yourself questioning what products are best for your little one? We thought so. So do we! We are mamas here at Lumo Little Ones, and nothing is more important to us than the well-being of our little ones. 100% organic bamboo is the best of the best for our bundles of joy, being ultra soft, antibacterial, hypoallergenic, free of dyes & chemicals, and 3x more absorbent than cotton. These towels will leave your baby cozy, dry, and happily wrapped up in a silky soft embrace after bath time. From our mama hearts, to yours.

Care Instructions:
-Machine Wash
-Hand Wash
-Do not Dry Clean
-Do not Bleach
-Do not Tumble Dry

Additional Care Tips:
-Wash before first use
-Do not store wet bath towel
-Store in a well aired room (never in a sealed container, plastic bag, etc)
-Avoid contact with rough surfaces which could loosen the yarns
-Do not bleach or use fabric softeners. Dryer sheets are also not recommended
-Keep away from open flames or electric heaters
-If towel is used after swimming pools, sea water, chlorinated water, please be sure to wash immediately after to prevent the bamboo fibre from weakening

Designed in the US, Made in China
Lumo Little Ones
info@lumolittleones.com

Target Market(s)

Moms

Industry/Entity Type

Baby

Font styles to use
Serif
Script

Colors
85cae6
eea4c8
ecf7fb
ffffff
d9d9d9
fdf9cf
cadf82
eaf2ce

Requirements
Must have
• the key info written in project description, our logo, company name, where it's made
Nice to have
• designs that communicate organic, purity & safety
• the yellow & green do not need to be used. If you have an idea and would like to include those colors, we have selected a yellow and two greens that would work with our vision. If you feel otherwise, please let us know why :)
Should not have
• it cannot look busy

```html
<!DOCTYPE html>
<html lang="en">
<head>
<meta charset="utf-8">
<title>Lumo Little Ones – Organic Bamboo Hooded Baby Bath Towels Box</title>
<link href="https://fonts.googleapis.com/css2?family=Quicksand:wght@400;500;600;700&display=swap" rel="stylesheet">
<style>
  :root{
    --ink:#3a3a3a;
    --gray:#6b6b6b;
    --line:#2b2b2b;
    --blue:#12aee8;
    --pink:#f4a9cd;
    --sky-light:#e3f1f8;
    --sky-mid:#a9d4ea;
    --white:#ffffff;
  }
  *{margin:0;padding:0;box-sizing:border-box}
  html,body{width:1200px;height:853px;overflow:hidden;background:var(--white)}
  body{position:relative;font-family:'Quicksand',sans-serif;color:var(--ink)}
  .panel{position:absolute;border:1.5px solid var(--line);background:var(--white)}
  .flap-top{left:51px;top:80px;width:412px;height:121px}
  .front{left:51px;top:199px;width:412px;height:571px;overflow:hidden}
  .side-left{left:461px;top:199px;width:139px;height:571px}
  .back{left:598px;top:199px;width:412px;height:571px}
  .side-right{left:1008px;top:199px;width:138px;height:571px}

  .brand{font-family:'Quicksand',sans-serif;font-weight:500;color:var(--blue);font-size:24px;letter-spacing:.3px;display:flex;align-items:center;gap:6px;white-space:nowrap}
  .brand-dot{width:9px;height:9px;border-radius:50%;background:var(--pink)}
  .flap-top .brand{position:absolute;left:50%;top:50%;transform:translate(-50%,-50%) rotate(180deg)}
  .front .brand{position:absolute;left:50%;top:54px;transform:translateX(-50%)}

  .title{position:absolute;left:0;width:100%;text-align:center}
  .title-main{top:106px;font-size:29px;font-weight:500;color:#6a6a6a;letter-spacing:.2px}
  .title-sub{top:145px;font-size:18px;font-weight:500;color:var(--pink);letter-spacing:.5px}

  .photo{position:absolute;left:62px;top:199px;width:278px;height:230px;background:radial-gradient(ellipse at 50% 55%,var(--sky-mid) 0%,var(--sky-light) 60%,var(--white) 100%)}

  .features{position:absolute;left:0;top:449px;width:100%;list-style:none;text-align:center}
  .features li{font-size:11.5px;font-weight:600;color:var(--blue);line-height:18.8px}
  .features li::before{content:"";display:inline-block;width:7px;height:7px;border-radius:50%;background:var(--pink);margin-right:9px;vertical-align:1px}

  .band-blue{position:absolute;left:0;bottom:16px;width:100%;height:6px;background:var(--blue)}
  .band-pink{position:absolute;left:0;bottom:0;width:100%;height:16px;background:var(--pink);color:var(--white);font-size:8.5px;text-align:center;line-height:16px;padding-right:56px}
  .badge{position:absolute;left:352px;top:527px;width:40px;height:40px;border-radius:50%;background:var(--blue);color:var(--white);font-size:5.6px;line-height:5.8px;text-align:center;display:flex;align-items:center;justify-content:center;padding:0 4px}

  .story{position:absolute;left:39px;top:52px;width:330px;font-size:12px;line-height:16px;color:var(--ink)}
  .care{position:absolute;left:39px;width:320px;font-size:8.8px;line-height:11.7px;color:var(--ink)}
  .care .label{color:var(--blue);font-weight:500}
  .care-main{top:267px}
  .care-icons{position:absolute;left:39px;top:300px}
  .care-tips{top:347px}
  .origin{position:absolute;left:39px;top:454px;font-size:8.8px}
  .contact{position:absolute;left:39px;top:538px;font-size:7.5px}
</style>
</head>
<body>
  <section class="panel flap-top">
    <div class="brand"><span class="brand-dot"></span>Lumo Little Ones</div>
  </section>

  <section class="panel front">
    <div class="brand"><span class="brand-dot"></span>Lumo Little Ones</div>
    <h1 class="title title-main">Organic Bamboo Hooded</h1>
    <h2 class="title title-sub">BABY BATH TOWELS</h2>
    <div class="photo" role="img" aria-label="Photo of a baby crawling under a light blue hooded bamboo bath towel"></div>
    <ul class="features">
      <li>Unbleached, chemical &amp; toxin free</li>
      <li>Hypoallergenic and Antibacterial</li>
      <li>Three times more absorbent than cotton</li>
      <li>Eco Friendly</li>
    </ul>
    <div class="band-blue"></div>
    <div class="band-pink">30X30 INCHES</div>
    <div class="badge">Includes bonus wash cloth</div>
  </section>

  <section class="panel side-left"></section>

  <section class="panel back">
    <p class="story">Do you ever find yourself questioning what products are best for your little one? We thought so. So do we! We are mamas here at Lumo Little Ones, and nothing is more important to us than the well-being of our little ones. 100% organic bamboo is the best of the best for our bundles of joy, being ultra soft, antibacterial, hypoallergenic, free of dyes &amp; chemicals, and 3x more absorbent than cotton. These towels will leave your baby cozy, dry, and happily wrapped up in a silky soft embrace after bath time. From our mama hearts, to yours.</p>

    <p class="care care-main"><span class="label">Care Instructions:</span> -Machine Wash-Hand Wash-Do not Dry Clean-Do not Bleach-Do not Tumble Dry</p>

    <svg class="care-icons" width="165" height="26" viewBox="0 0 165 26" fill="none" stroke="#3a3a3a" stroke-width="1.3" aria-label="Care symbols">
      <path d="M1 5 L5 23 H24 L28 5"/>
      <path d="M2 8 q3.5 -3 7 0 q3.5 3 7 0 q3.5 -3 7 0 q3 2.5 5 0"/>
      <text x="9" y="20" font-size="8" font-family="Quicksand, sans-serif" fill="#3a3a3a" stroke="none">40°</text>
      <path d="M34 23 L46 3 L58 23 Z"/>
      <path d="M35 4 L57 24 M57 4 L35 24"/>
      <path d="M70 24 H92 V10 H79 Q71 12 70 24 Z"/>
      <path d="M75 16 H92"/>
      <circle cx="84" cy="20" r="1.3" fill="#3a3a3a" stroke="none"/>
      <circle cx="110" cy="14" r="11"/>
      <text x="105.5" y="18.5" font-size="12" font-family="Quicksand, sans-serif" fill="#3a3a3a" stroke="none">P</text>
      <rect x="139" y="2" width="23" height="23"/>
      <circle cx="150.5" cy="13.5" r="10"/>
    </svg>

    <p class="care care-tips"><span class="label">Additional Care Tips:</span>-Wash before first use-Do not store wet bath towel-Store in a well aired room (never in a sealed container, plastic bag, etc)-Avoid contact with rough surfaces which could loosen the yarns-Do not bleach or use fabric softeners. Dryer sheets are also not recommended-Keep away from open flames or electric heaters-If towel is used after swimming pools, sea water, chlorinated water, please be sure to wash immediately after to prevent the bamboo fibre from weakening</p>

    <p class="origin">Designed in the US, Made in China</p>
    <p class="contact">Lumo Little Ones info@lumolittleones.com</p>
  </section>

  <section class="panel side-right"></section>
</body>
</html>
```